Trading journal (Ledger Lens)

I need a design for trading journal application.
I would like to start from dark version of the design and the main goal that it should be pretty intuitive for everyone. I am going to create the app from scratch and I don't have any logo or branding colors, so it is up to you to choose a color scheme but it is a dark mode, so one of the colors would be black obviously.
The app will be available for web PC, Android and iOS.

There is google document with the requirements.
https://files.brimvault.example/doc/7KpTzR2wQx9LmNc4VbHs8JdYf3GaUe6Wo1XiRq5Zt0Ay/view?mode=share

Target Market(s)

Professional traders

Industry/Entity Type

Trading

Colors

Designer to choose colors to be used in the design.

Requirements
Must have
• Dark mode design for PC and mobile views, the design must be pretty intuitive for everyone.
Nice to have
• Tooltips for something non obvious; popovers after completing some actions

```html
<!DOCTYPE html>
<html lang="en">
<head>
<meta charset="utf-8">
<title>Ledger Lens – Dashboard</title>
<link rel="stylesheet" href="https://fonts.googleapis.com/css2?family=Outfit:wght@300;400;500&display=swap">
<style>
:root{
  --bg:#000;
  --panel:#18191b;
  --panel-2:#222326;
  --text:#fff;
  --muted:#8a8d93;
  --accent:#3355f1;
  --card-green:#b9fbc0;
  --card-red:#fd8080;
  --card-sky:#5dabfb;
  --ink:#1d2a4a;
  --ink-soft:#4a5a6a;
  --up:#19d46a;
  --down:#ff2a2a;
  --line:#14f214;
  --grid:#2a2c30;
}
*{box-sizing:border-box;margin:0;padding:0}
html,body{width:1200px;height:900px;overflow:hidden;background:var(--bg);font-family:"Outfit",sans-serif;color:var(--text)}
.canvas{position:relative;width:1200px;height:900px}
.abs{position:absolute}
.topbar{left:62px;top:59px;width:1054px;height:71px;background:var(--panel);border-radius:12px}
.search{left:562px;top:21px;width:246px;height:31px;background:var(--panel-2);border-radius:8px;display:flex;align-items:center;gap:8px;padding-left:12px;color:var(--muted);font-size:12px;font-weight:300}
.round-btn{top:21px;width:30px;height:30px;border-radius:50%;background:var(--panel-2);display:flex;align-items:center;justify-content:center}
.avatar{left:945px;top:21px;width:30px;height:30px;border-radius:50%;background:linear-gradient(135deg,#d9a23b,#3f8c6b)}
.greet{left:988px;top:27px;font-size:11px}
.crumb{left:168px;top:165px;font-size:9.5px;color:#3d63ff}
.sidebar{left:62px;top:196px;width:58px;height:552px;background:var(--panel);border-radius:12px}
.sidebar .active-bar{left:0;top:20px;width:5px;height:40px;background:var(--accent);border-radius:0 3px 3px 0}
.sidebar svg{position:absolute;left:17px;width:24px;height:24px;fill:none;stroke:#fff;stroke-width:1.6;stroke-linecap:round;stroke-linejoin:round}
.welcome{left:168px;top:196px;width:215px;height:258px;background:var(--accent);border-radius:13px}
.welcome .time{left:69px;top:42px;font-size:25px;font-weight:400}
.welcome .hello{left:71px;top:72px;font-size:11px;color:#a9bcff}
.welcome .today{left:25px;top:127px;font-size:15px;line-height:20px;font-weight:500}
.welcome .sync{left:25px;top:208px;font-size:11px;font-weight:500}
.stat{width:214px;height:114px;border-radius:13px;color:var(--ink)}
.stat.green{background:var(--card-green)}
.stat.red{background:var(--card-red)}
.stat.sky{background:var(--card-sky)}
.stat .value{position:absolute;left:22px;top:16px;font-size:31px;font-weight:400}
.stat .label{position:absolute;left:22px;top:64px;font-size:14px}
.stat .sub{position:absolute;left:22px;top:86px;font-size:10.5px;color:var(--ink-soft);display:flex;align-items:center;gap:5px;font-weight:300}
.stat .dot{width:11px;height:11px;border-radius:50%}
.stat .badge{position:absolute;right:18px;top:14px;width:36px;height:36px;border-radius:50%;display:flex;align-items:center;justify-content:center}
.green .badge{background:#5f8c68}
.red .badge{background:#a65a5d}
.sky .badge{background:#3e6aa3}
.badge svg{width:20px;height:20px;fill:none;stroke:#fff;stroke-width:1.7;stroke-linecap:round;stroke-linejoin:round}
.chart{left:164px;top:489px;width:624px;height:295px;background:var(--panel);border-radius:13px}
.chart-title{left:23px;top:26px;font-size:14px}
.legend{top:28px;font-size:12.5px;font-weight:300;color:#cfd1d4}
.legend.on{color:var(--line)}
.coins{left:805px}
.coin{left:805px;width:311px;height:58px;background:var(--panel);border-radius:12px}
.coin .mark{position:absolute;left:11px;top:10px;width:38px;height:38px;border-radius:50%}
.coin .name{position:absolute;left:61px;top:13px;font-size:13px}
.coin .tick{position:absolute;left:61px;top:33px;font-size:10px;color:var(--muted)}
.coin .spark{position:absolute;left:125px;top:12px;width:50px;height:28px}
.coin .state{position:absolute;left:187px;top:13px;font-size:13.5px;font-style:italic}
.coin .price{position:absolute;right:10px;top:13px;font-size:13px;font-style:italic}
.coin .chg{position:absolute;right:12px;top:35px;font-size:8px}
.up{color:var(--up)}
.down{color:var(--down)}
</style>
</head>
<body>
<div class="canvas">

  <header class="abs topbar">
    <div class="abs search">
      <svg width="13" height="13" viewBox="0 0 24 24" fill="none" stroke="#fff" stroke-width="2.4"><circle cx="11" cy="11" r="7"/><path d="M16 16l5 5"/></svg>
      Quick Search...
    </div>
    <div class="abs round-btn" style="left:853px">
      <svg width="15" height="15" viewBox="0 0 24 24" fill="none" stroke="#fff" stroke-width="1.8"><rect x="3" y="5" width="18" height="16" rx="3"/><path d="M8 3v4M16 3v4M3 10h18M8 14h1M12 14h1M16 14h1M8 17h1M12 17h1M16 17h1"/></svg>
    </div>
    <div class="abs round-btn" style="left:898px">
      <svg width="15" height="15" viewBox="0 0 24 24" fill="none" stroke="#fff" stroke-width="1.8"><path d="M6 17V11a6 6 0 0 1 12 0v6l2 2H4zM10 21h4"/><circle cx="17" cy="5" r="3" fill="#5aa8ff" stroke="none"/></svg>
    </div>
    <div class="abs avatar" role="img" aria-label="User profile photo"></div>
    <div class="abs greet">Hi Ravin!</div>
  </header>

  <div class="abs crumb">Dashboard ◢</div>

  <nav class="abs sidebar">
    <div class="abs active-bar"></div>
    <svg style="top:28px;stroke:#3d63ff;stroke-width:2.2" viewBox="0 0 24 24"><rect x="3" y="3" width="7" height="7" rx="2"/><rect x="14" y="3" width="7" height="7" rx="2"/><rect x="3" y="14" width="7" height="7" rx="2"/><rect x="14" y="14" width="7" height="7" rx="2"/></svg>
    <svg style="top:85px" viewBox="0 0 24 24"><rect x="3" y="3" width="18" height="18" rx="5"/><path d="M7 14l3-3 3 2 4-4"/></svg>
    <svg style="top:136px" viewBox="0 0 24 24"><circle cx="8" cy="8" r="4"/><circle cx="15" cy="14" r="6"/><circle cx="7" cy="17" r="3"/></svg>
    <svg style="top:186px" viewBox="0 0 24 24"><circle cx="12" cy="12" r="9"/><circle cx="12" cy="12" r="3.5"/></svg>
    <svg style="top:237px" viewBox="0 0 24 24"><path d="M12 6C9 4 6 4 3 5v14c3-1 6-1 9 1 3-2 6-2 9-1V5c-3-1-6-1-9 1zM12 6v14M6 9h3M6 12h3"/></svg>
    <svg style="top:288px" viewBox="0 0 24 24"><circle cx="12" cy="7" r="4"/><path d="M4 21c0-4 4-7 8-7s8 3 8 7"/></svg>
    <svg style="top:338px" viewBox="0 0 24 24"><rect x="3" y="5" width="18" height="15" rx="4"/><path d="M21 10h-4a2.5 2.5 0 0 0 0 5h4"/></svg>
    <svg style="top:388px" viewBox="0 0 24 24"><rect x="3" y="5" width="18" height="16" rx="1"/><path d="M8 3v4M16 3v4M3 10h18"/></svg>
    <svg style="top:441px" viewBox="0 0 24 24"><path d="M12 2l8.5 5v10L12 22l-8.5-5V7z"/><circle cx="12" cy="12" r="3"/></svg>
    <svg style="top:494px" viewBox="0 0 24 24"><circle cx="12" cy="12" r="9.5"/><path d="M9.5 9.5a2.5 2.5 0 1 1 3.5 2.3c-.7.4-1 .9-1 1.7M12 17h.01"/></svg>
  </nav>

  <section class="abs welcome">
    <svg class="abs" style="left:19px;top:43px" width="44" height="44" viewBox="0 0 44 44" fill="none" stroke="#fff" stroke-width="3" stroke-linecap="round"><circle cx="22" cy="22" r="9"/><path d="M22 4v4M22 36v4M4 22h4M36 22h4M9 9l3 3M32 32l3 3M9 35l3-3M32 12l3-3"/></svg>
    <div class="abs time">8:02:09 AM</div>
    <div class="abs hello">Good Morning Ravin !</div>
    <div class="abs today">Today:<br>15th January 2024</div>
    <div class="abs sync">Last synced 1 minute ago !</div>
  </section>

  <article class="abs stat green" style="left:413px;top:196px">
    <div class="value">$478.0</div>
    <div class="label">Total net Profit</div>
    <div class="sub"><span class="dot" style="background:#f0b7b7"></span>+3% Descrease than yesterday</div>
    <div class="badge"><svg viewBox="0 0 24 24"><circle cx="12" cy="12" r="9"/><path d="M15 9.5c-.5-1-1.6-1.5-3-1.5-1.7 0-3 .8-3 2s1.3 1.7 3 2 3 .8 3 2-1.3 2-3 2c-1.4 0-2.5-.5-3-1.5M12 6v12"/></svg></div>
  </article>
  <article class="abs stat green" style="left:656px;top:196px">
    <div class="value">$507.6</div>
    <div class="label">Average Win</div>
    <div class="sub"><span class="dot" style="background:#8ef08a"></span>Daily</div>
    <div class="badge"><svg viewBox="0 0 24 24"><rect x="5" y="3" width="14" height="18" rx="2"/><path d="M8 7h8M8 11h1M12 11h1M15 11h1M8 14h1M12 14h1M15 14h1M8 17h1M12 17h1M15 17h1"/></svg></div>
  </article>
  <article class="abs stat green" style="left:902px;top:196px">
    <div class="value">79%</div>
    <div class="label">Today Win Rate</div>
    <div class="sub"><span class="dot" style="background:#f0b7b7"></span>+3% Increase than yesterday</div>
    <div class="badge"><svg viewBox="0 0 24 24"><path d="M18 6L6 18"/><circle cx="7" cy="7" r="2"/><circle cx="17" cy="17" r="2"/></svg></div>
  </article>
  <article class="abs stat red" style="left:413px;top:340px">
    <div class="value">$31.0</div>
    <div class="label">Today Fees &amp; Commissions</div>
    <div class="sub"><span class="dot" style="background:#f7b0b0"></span>+3% Increase than yesterday</div>
    <div class="badge"><svg viewBox="0 0 24 24"><path d="M4 4v16h16M7 15l4-5 3 3 5-6"/></svg></div>
  </article>
  <article class="abs stat sky" style="left:656px;top:340px">
    <div class="value">6</div>
    <div class="label">Trades</div>
    <div class="sub"><span class="dot" style="background:#7a8cf5"></span>number of Ongoing Trades</div>
    <div class="badge"><svg viewBox="0 0 24 24" style="fill:#fff;stroke:none"><circle cx="14" cy="8" r="4"/><circle cx="8" cy="15" r="3"/><circle cx="16.5" cy="16.5" r="2.5"/></svg></div>
  </article>
  <article class="abs stat sky" style="left:902px;top:340px">
    <div class="value">$19289.1</div>
    <div class="label">total Assets</div>
    <div class="sub"><span class="dot" style="background:#9cc8f6"></span>wallet balance</div>
    <div class="badge"><svg viewBox="0 0 24 24"><path d="M12 3l8 4.5v9L12 21l-8-4.5v-9z"/><path d="M12 8l4 2.2v4.6L12 17l-4-2.2v-4.6z"/></svg></div>
  </article>

  <section class="abs chart">
    <div class="abs chart-title">Profit &amp; Loss Graph</div>
    <div class="abs legend on" style="left:366px"><span style="display:inline-block;width:7px;height:7px;border-radius:50%;background:var(--line);margin-right:5px"></span>Daily</div>
    <div class="abs legend" style="left:426px">o Weekly</div>
    <div class="abs legend" style="left:492px">o Monthly</div>
    <svg class="abs" style="left:586px;top:27px" width="16" height="18" viewBox="0 0 16 18" fill="none" stroke="#fff" stroke-width="1.4"><path d="M1 3h14M1 9h14M1 15h14"/><circle cx="10" cy="3" r="2" fill="#18191b"/><circle cx="5" cy="9" r="2" fill="#18191b"/><circle cx="9" cy="15" r="2" fill="#18191b"/></svg>
    <svg class="abs" style="left:0;top:0" width="624" height="295" viewBox="0 0 624 295" font-family="Outfit, sans-serif">
      <defs>
        <linearGradient id="area" x1="0" y1="0" x2="0" y2="1">
          <stop offset="0" stop-color="#2a3a8a" stop-opacity=".55"/>
          <stop offset="1" stop-color="#18191b" stop-opacity="0"/>
        </linearGradient>
      </defs>
      <g stroke="var(--grid)" stroke-width="1">
        <path d="M60 83H598M60 113.6H598M60 144.2H598M60 174.8H598M60 205.4H598M60 236H598"/>
        <path d="M60 83V236M106 83V236M153 83V236M199 83V236M246 83V236M292 83V236M339 83V236M385 83V236M431 83V236M478 83V236M525 83V236M571 83V236"/>
      </g>
      <g fill="#9a9ca0" font-size="8" text-anchor="end">
        <text x="47" y="86">$500</text><text x="47" y="116">$400</text><text x="47" y="147">$300</text>
        <text x="47" y="177">$200</text><text x="47" y="208">$100</text><text x="47" y="239">0</text>
      </g>
      <g fill="#3c3e43" font-size="8" text-anchor="middle">
        <text x="75" y="263">01 Aug</text><text x="121" y="263">02 Aug</text><text x="168" y="263">03 Aug</text><text x="214" y="263">04 Aug</text>
        <text x="261" y="263">07 Aug</text><text x="307" y="263">08 Aug</text><text x="354" y="263">09 Aug</text><text x="400" y="263">10 Aug</text>
        <text x="446" y="263">11 Aug</text><text x="493" y="263">14 Aug</text><text x="540" y="263">15 Aug</text><text x="586" y="263">16 Aug</text>
      </g>
      <path d="M61.7 146.8C84 134 92 126 106.2 126.2C122 126 130 146 152.8 146.3C175 146 185 134 199.5 123.5C214 112 230 108 246.1 109.9C266 112 268 150 292.2 152.8C314 155 322 126 338.9 125.7C358 126 362 177 384.5 177.2C408 177 414 152 431.1 144.1C450 135 462 125 478.3 125.7C500 127 510 137 525 145.7C545 158 555 176 571.6 175.6C588 175 594 150 598.2 136.5L598 236H61.7Z" fill="url(#area)"/>
      <rect x="236" y="110" width="19" height="128" fill="#1f6b1f" opacity=".75"/>
      <path d="M61.7 146.8C84 134 92 126 106.2 126.2C122 126 130 146 152.8 146.3C175 146 185 134 199.5 123.5C214 112 230 108 246.1 109.9C266 112 268 150 292.2 152.8C314 155 322 126 338.9 125.7C358 126 362 177 384.5 177.2C408 177 414 152 431.1 144.1C450 135 462 125 478.3 125.7C500 127 510 137 525 145.7C545 158 555 176 571.6 175.6C588 175 594 150 598.2 136.5" fill="none" stroke="var(--line)" stroke-width="1.6"/>
      <g fill="#18191b" stroke="var(--line)" stroke-width="1.1">
        <circle cx="61.7" cy="146.8" r="3"/><circle cx="106.2" cy="126.2" r="3"/><circle cx="152.8" cy="146.3" r="3"/>
        <circle cx="199.5" cy="123.5" r="3"/><circle cx="292.2" cy="152.8" r="3"/><circle cx="338.9" cy="125.7" r="3"/>
        <circle cx="384.5" cy="177.2" r="3"/><circle cx="431.1" cy="144.1" r="3"/><circle cx="478.3" cy="125.7" r="3"/>
        <circle cx="525" cy="145.7" r="3"/><circle cx="571.6" cy="175.6" r="3"/>
      </g>
      <circle cx="246.1" cy="109.9" r="5" fill="var(--line)"/>
      <circle cx="246.1" cy="109.9" r="1.8" fill="#0c3a0c"/>
      <text x="251" y="95" fill="#a0a3a8" font-size="11" text-anchor="middle">$417</text>
    </svg>
  </section>

  <div class="abs coin" style="top:486px">
    <span class="mark" style="background:#f7931a"></span>
    <span class="name">Corvex</span><span class="tick">CVX</span>
    <svg class="spark" viewBox="0 0 50 28" fill="none" stroke="var(--up)" stroke-width="1.1"><path d="M0 16l3 8 4-10 3 6 4-9 3 5 3-7 3 12 3-14 3 8 4-9 3 6 4-8 3 6 3-5"/></svg>
    <span class="state up">Open</span>
    <span class="price">$4637.99</span><span class="chg up">+9.77%</span>
  </div>
  <div class="abs coin" style="top:554px">
    <span class="mark" style="background:#6a7ff0"></span>
    <span class="name">Aetherion</span><span class="tick">AER</span>
    <svg class="spark" viewBox="0 0 50 28" fill="none" stroke="var(--down)" stroke-width="1.1"><path d="M0 24l5-4 4 6 4-18 4 12 4-9 3 5 4-8 4 6 4-7 5 10"/></svg>
    <span class="state up">Open</span>
    <span class="price">$4637.99</span><span class="chg down">-1.13%</span>
  </div>
  <div class="abs coin" style="top:623px">
    <span class="mark" style="background:#e51a23"></span>
    <span class="name">Vaultra</span><span class="tick">VLT</span>
    <svg class="spark" viewBox="0 0 50 28" fill="none" stroke="var(--down)" stroke-width="1.1"><path d="M0 20l5-10 4 8 4-6 4 7 4-9 3 12 4-8 4 12 4-2 5 1"/></svg>
    <span class="state down" style="top:5px">Closed</span>
    <span class="price">$4637.99</span><span class="chg down">-3.34%</span>
  </div>
  <div class="abs coin" style="top:692px">
    <span class="mark" style="background:#f7931a"></span>
    <span class="name">Corvex</span><span class="tick">CVX</span>
    <svg class="spark" viewBox="0 0 50 28" style="left:113px" fill="none" stroke="var(--up)" stroke-width="1.1"><path d="M0 16l3 8 4-10 3 6 4-9 3 5 3-7 3 12 3-14 3 8 4-9 3 6 4-8 3 6 3-5"/></svg>
    <span class="state up">Open</span>
    <span class="price">$4637.99</span><span class="chg up">+9.77%</span>
  </div>
  <svg class="abs" style="left:961px;top:769px" width="12" height="10" viewBox="0 0 12 10" fill="none" stroke="#fff" stroke-width="1.6"><path d="M1 2l5 5 5-5"/></svg>

</div>
</body>
</html>
```